Professional Modern Website Design

We are a premium IT services provider to the financial industry based in London. Our company is called Veltra our current holding page is www.veltra-example.co.uk. We require a new website to match our new corporate identity. This project is for the design phase only. Development will be handled in-house. I have attached examples of wire frames we have developed (although open to suggestions for improvement) Our brand document that should demonstrate current brand, inc how we communicate to potential clients and finally mostly completed web-content.
We are looking for designers that can create something that sets us apart from our competitors.
Target Market(s)
IT Decision makers in Finance companies such as; hedge funds, private investment banks etc
Industry/Entity Type
Financial
Number of Pages Required
5+ page
Requirements
Must have
- hexagon elements in the design, unique design.
Nice to have
- Blog and social media feeds
Should not have
- Should not resemble a downloaded template

```html
<!DOCTYPE html>
<html lang="en">
<head>
<meta charset="utf-8">
<title>Veltra — IT services for finance</title>
<link href="https://fonts.googleapis.com/css2?family=Open+Sans:wght@300;400;600&family=Arimo:wght@400&display=swap" rel="stylesheet">
<style>
:root{
  --header:#4b4a4d;
  --nav:#dcdcdc;
  --orange:#f39229;
  --dark-box:#353435;
  --text:#3a3a3a;
  --muted:#555;
  --blog-bg:#ebebeb;
  --footer:#3d3d3f;
}
*{margin:0;padding:0;box-sizing:border-box}
html,body{width:966px;height:1200px;overflow:hidden}
body{font-family:"Open Sans",sans-serif;color:var(--text);position:relative;background:#fff}
.abs{position:absolute}
.site-header{left:0;top:0;width:966px;height:94px;background:var(--header)}
.brand{left:134px;top:12px;display:flex;flex-direction:column;align-items:center;gap:8px}
.brand-mark{width:42px;height:42px;background:var(--orange)}
.brand-name{color:#d8d8d8;font-size:10px;letter-spacing:4px;text-transform:uppercase}
.social-top{left:714px;top:35px;display:flex;gap:7px}
.social-top span{width:22px;height:22px;border-radius:50%;display:block;box-shadow:inset 0 -2px 0 rgba(0,0,0,.15)}
.main-nav{left:0;top:94px;width:966px;height:31px;background:var(--nav);border-bottom:3px solid #555}
.main-nav a{position:absolute;top:0;height:28px;line-height:28px;font-family:"Arimo",sans-serif;font-size:12px;color:#333;text-decoration:none}
.main-nav a.active{background:var(--orange);width:64px;text-align:center}
.dropdown{left:568px;top:126px;width:222px;height:151px;background:linear-gradient(160deg,#f8a233,#f38b23);padding:10px 0 0 14px;opacity:.96}
.dropdown li{list-style:none;color:#fff;font-size:10.3px;line-height:16px;margin-bottom:8px;padding-left:18px;position:relative}
.dropdown li::before{content:"»";position:absolute;left:0;top:-1px}
.hero{left:0;top:128px;width:966px;height:321px;
  background:
    radial-gradient(ellipse 260px 90px at 90px 230px, rgba(120,150,185,.75), transparent 70%),
    radial-gradient(ellipse 420px 160px at 760px 230px, rgba(150,110,80,.55), transparent 70%),
    radial-gradient(ellipse 300px 80px at 880px 300px, rgba(70,95,55,.7), transparent 70%),
    linear-gradient(180deg,#dfe7ef 0%,#c3ccd6 22%,#9a9890 45%,#8a7866 62%,#6f6a5c 80%,#5a6648 100%)}
.hero-card{left:115px;top:182px;width:373px;height:210px;background:var(--dark-box);padding:22px 25px 0 24px}
.hero-card h1{font-weight:400;font-size:15.5px;line-height:23px;color:#fff;width:300px}
.hero-card p{font-size:9.4px;line-height:18px;color:#cfcfcf;margin-top:16px;padding-left:2px;letter-spacing:-.05px}
.btn-about{display:inline-block;margin:20px 0 0 2px;background:#5a5a5a;color:#fff;font-size:11.5px;width:96px;height:29px;line-height:29px;text-align:center}
.slider-arrow{top:274px;width:26px;height:26px}
.audience{left:0;top:449px;width:966px;height:414px;background:linear-gradient(180deg,#fff3ea 0%,#fcd6ae 60%,#fdc98d 100%)}
.audience h2{position:absolute;top:27px;width:966px;text-align:center;font-weight:400;font-size:17px;color:#333}
.audience .lead{position:absolute;top:59px;left:220px;width:526px;text-align:center;font-size:11.3px;line-height:19px;color:#555}
.persona{top:127px;width:160px;text-align:center}
.persona svg{display:block;margin:0 auto}
.persona h3{font-weight:400;font-size:12px;line-height:17px;color:#333;margin-top:12px}
.persona p{font-size:8.6px;line-height:15px;color:#555;margin:6px auto 0;width:152px}
.read-more{color:var(--orange);font-size:8.6px;margin-top:7px;display:block}
.blog{left:0;top:863px;width:966px;height:254px;background:var(--blog-bg)}
.blog h2{position:absolute;left:115px;top:24px;font-weight:400;font-size:18.5px;color:#333}
.post{top:59px;width:162px}
.post-image{width:162px;height:84px;border:2px solid #fff;box-shadow:0 0 2px #bbb}
.post p{font-size:8.6px;line-height:14.5px;color:#555;margin-top:7px;padding-left:1px}
.post .read-more{margin-top:9px}
.follow{left:659px;width:191px;height:169px;background:var(--orange)}
.follow h4{position:absolute;left:12px;top:13px;font-weight:400;font-size:10px;color:#fff}
.follow-panel{position:absolute;left:9px;top:38px;width:173px;height:123px;background:#fff;border-radius:3px;padding:8px 9px;display:grid;grid-template-columns:76px 76px;gap:5px 6px}
.tile{height:22px;color:#fff;display:flex;align-items:center;gap:7px;padding-left:5px}
.tile i{width:10px;height:10px;border:1.5px solid rgba(255,255,255,.9);border-radius:50%;display:block;flex:none}
.tile b{font-weight:400;font-size:6.5px;line-height:7px}
.tile small{display:block;font-size:4.8px}
.t-blue{background:#3b65a8}.t-orange{background:#f7971f}.t-sky{background:#2f86c4}.t-pink{background:#e9477e}.t-red{background:#d93636}
.site-footer{left:0;top:1117px;width:966px;height:83px;background:var(--footer)}
.footer-links{position:absolute;left:115px;top:22px;font-size:9.5px;color:#e6e6e6}
.footer-links span{margin:0 6px;color:#aaa}
.copyright{position:absolute;left:115px;top:40px;font-size:10px;color:#e6e6e6}
</style>
</head>
<body>

<header class="site-header abs">
  <div class="brand abs"><span class="brand-mark"></span><span class="brand-name">Veltra</span></div>
  <div class="social-top abs">
    <span style="background:#3b5a9a"></span><span style="background:#28a3e0"></span><span style="background:#1a7bb9"></span><span style="background:#e23b2e"></span><span style="background:#f59a23"></span>
  </div>
</header>

<nav class="main-nav abs">
  <a style="left:430px">Home</a>
  <a style="left:500px">About us</a>
  <a class="active" style="left:568px">Services</a>
  <a style="left:653px">Partners</a>
  <a style="left:728px">Clients</a>
  <a style="left:795px">Contact us</a>
</nav>

<section class="hero abs" role="img" aria-label="City skyline with bridges and a river"></section>

<ul class="dropdown abs">
  <li>Data Centre &amp; Infrastructure</li>
  <li>Support, Managed &amp; Professional Services</li>
  <li>Voice and Data</li>
  <li>Hosting and Cloud</li>
  <li>Security and IRM</li>
</ul>

<div class="hero-card abs">
  <h1>You need integration. We’re always there with you.</h1>
  <p>Veltra is one of the leading systems integrators to the world’s finance sector. We are an extension of your business and our services portfolio has been built so you always have access to a complete partner.</p>
  <span class="btn-about">ABOUT US</span>
</div>

<svg class="slider-arrow abs" style="left:45px" viewBox="0 0 26 26"><circle cx="13" cy="13" r="11.5" fill="rgba(0,0,0,.15)" stroke="#fff" stroke-width="1.6"/><path d="M16 7 L9 13 L16 19 L14 13 Z" fill="#fff"/></svg>
<svg class="slider-arrow abs" style="left:899px" viewBox="0 0 26 26"><circle cx="13" cy="13" r="11.5" fill="rgba(0,0,0,.15)" stroke="#fff" stroke-width="1.6"/><path d="M10 7 L17 13 L10 19 L12 13 Z" fill="#fff"/></svg>

<svg width="0" height="0" class="abs">
  <defs>
    <radialGradient id="hexWarm" cx="50%" cy="45%" r="60%"><stop offset="0" stop-color="#f4f1ee"/><stop offset=".6" stop-color="#ffffff"/><stop offset="1" stop-color="#dfe2e6"/></radialGradient>
    <radialGradient id="hexDark" cx="50%" cy="55%" r="60%"><stop offset="0" stop-color="#5b5d63"/><stop offset=".45" stop-color="#c9cacd"/><stop offset="1" stop-color="#ffffff"/></radialGradient>
    <radialGradient id="hexCool" cx="50%" cy="50%" r="60%"><stop offset="0" stop-color="#c6cfdd"/><stop offset=".6" stop-color="#e8ecf2"/><stop offset="1" stop-color="#b9c3cf"/></radialGradient>
  </defs>
</svg>

<section class="audience abs">
  <h2>Who Are You?</h2>
  <p class="lead">If you’re part of a financial organisation, we have the power to help everyone work more efficiently, productively and profitably.</p>

  <div class="persona abs" style="left:127px">
    <svg width="118" height="134" viewBox="0 0 118 134" role="img" aria-label="Portrait of a senior hedge fund manager"><polygon points="59,1 117,34 117,100 59,133 1,100 1,34" fill="url(#hexWarm)" stroke="#fff" stroke-width="2"/></svg>
    <h3>Senior Hedge Fund Manager/CEO</h3>
    <p>You need to develop and implement strategies for business growth, while ensuring profitability.</p>
    <span class="read-more">[ READ MORE ]</span>
  </div>
  <div class="persona abs" style="left:312px">
    <svg width="118" height="134" viewBox="0 0 118 134" role="img" aria-label="Portrait of a CFO"><polygon points="59,1 117,34 117,100 59,133 1,100 1,34" fill="url(#hexDark)" stroke="#fff" stroke-width="2"/></svg>
    <h3>CFO</h3>
    <p>Your key responsibility is to obtain the maximum ROI from products and services.</p>
    <span class="read-more">[ READ MORE ]</span>
  </div>
  <div class="persona abs" style="left:495px">
    <svg width="118" height="134" viewBox="0 0 118 134" role="img" aria-label="Portrait of an IT manager"><polygon points="59,1 117,34 117,100 59,133 1,100 1,34" fill="url(#hexDark)" stroke="#fff" stroke-width="2"/></svg>
    <h3>IT Manager/CTO</h3>
    <p>Integration with partners and ser­vices is your key concern. You want to make sure any IT</p>
    <span class="read-more">[ READ MORE ]</span>
  </div>
  <div class="persona abs" style="left:678px">
    <svg width="118" height="134" viewBox="0 0 118 134" role="img" aria-label="Portrait of employees in front of a world map"><polygon points="59,1 117,34 117,100 59,133 1,100 1,34" fill="url(#hexCool)" stroke="#fff" stroke-width="2"/></svg>
    <h3>Employees</h3>
    <p>You’re working hard, but not getting anywhere fast. You want the tools to make your job easier</p>
    <span class="read-more">[ READ MORE ]</span>
  </div>
</section>

<section class="blog abs">
  <h2>Latest From the Blog</h2>
  <article class="post abs" style="left:115px">
    <div class="post-image" role="img" aria-label="Business team celebrating in an office" style="background:radial-gradient(ellipse 60px 40px at 40px 60px,#9db4d6,transparent 70%),linear-gradient(135deg,#e4e8ee 0%,#a9b4c2 50%,#4f5866 100%)"></div>
    <p>Nemo enim ipsam voluptatem quia voluptas sit aspernatur aut odit aut fugit, sed quia  magni</p>
    <span class="read-more">[ READ MORE ]</span>
  </article>
  <article class="post abs" style="left:289px">
    <div class="post-image" role="img" aria-label="Colleagues in a meeting" style="background:radial-gradient(ellipse 70px 40px at 110px 55px,#2e3a4a,transparent 70%),linear-gradient(135deg,#eef3f7 0%,#b9cfdf 45%,#5e86aa 100%)"></div>
    <p>Nemo enim ipsam voluptatem quia voluptas sit aspernatur aut odit aut fugit, sed quia  magni</p>
    <span class="read-more">[ READ MORE ]</span>
  </article>
  <article class="post abs" style="left:465px">
    <div class="post-image" role="img" aria-label="Business people talking at a table" style="background:radial-gradient(ellipse 50px 50px at 110px 55px,#23252c,transparent 70%),linear-gradient(135deg,#f1efec 0%,#cfc7c0 45%,#6c6e78 100%)"></div>
    <p>Nemo enim ipsam voluptatem quia voluptas sit aspernatur aut odit aut fugit, sed quia  magni</p>
    <span class="read-more">[ READ MORE ]</span>
  </article>

  <aside class="follow abs" style="top:39px">
    <h4>FOLLOW US</h4>
    <div class="follow-panel">
      <div class="tile t-blue"><i></i><b>31758<small>Likes</small></b></div>
      <div class="tile t-orange"><i></i><b>Subscribe<small>RSS Feeds</small></b></div>
      <div class="tile t-sky"><i></i><b>1<small>Follower</small></b></div>
      <div class="tile t-pink"><i></i><b>9011<small>Followers</small></b></div>
      <div class="tile t-red"><i></i><b>2370279<small>Subscribers</small></b></div>
      <div class="tile t-orange"><i></i><b>0<small>Follower</small></b></div>
      <div class="tile t-red"><i></i><b>0<small>Follower</small></b></div>
      <div class="tile t-blue"><i></i><b>0<small>Follower</small></b></div>
    </div>
  </aside>
</section>

<footer class="site-footer abs">
  <div class="footer-links">Home <span>|</span> About Us <span>|</span> Services <span>|</span> Partners <span>|</span> Clients <span>|</span> Conatct us</div>
  <div class="copyright">Copy rights © Veltra . All rights reserved.</div>
</footer>

</body>
</html>
```